High value cover design for an A4 ideation pad.

The product is NOT A BOOK.

It's an A4 ideation pad for professionals, designers and creators who handwrite their ideas. Visualise creators like Marcus Tellwind, Owen Prackett and Dale Vorhanek in your mind's eye.

I'm looking for a cover design for the ideation pad. Both front and back.

It should look, feel and convey the following.

--> A handcrafted product experience

--> High value & Elegance

--> Inspiration

Mandatory --> See Uploaded Files --> Files 1, 5 & 6

Target Market(s)

- Designers

-Creative Professionals

- Entrepreneurs

who handwrite their ideas. Visualise creators like Marcus Tellwind, Owen Prackett and Dale Vorhanek in your mind's eye.

Industry/Entity Type

Stationary

Font styles to use
Script
Other font styles liked:
• Calligraphy

Colors
fbed22

Requirements
Must have
• Title text - Amber Lantern

-Text in gold on brown leather background to convey high value for the front cover.

--> High value & Elegance

--> Inspiration

--> Should compel the customers to pick up and own the idea pad
Nice to have
• That's my take but other ideas are welcome
Should not have
• Must not convey

- low value

```html
<!DOCTYPE html>
<html lang="en">
<head>
<meta charset="utf-8">
<title>Amber Lantern – Ideation Pad Cover</title>
<link rel="stylesheet" href="https://fonts.googleapis.com/css2?family=Parisienne&family=Marcellus&display=swap">
<style>
  :root {
    --cover-black: #0b0a0a;
    --cover-charcoal: #1c1a19;
    --grunge-grey: #3a3634;
    --binding-hole: #d9d9d9;
    --title-gold: #d8943a;
  }
  html, body {
    margin: 0;
    padding: 0;
    width: 927px;
    height: 1200px;
    overflow: hidden;
    background: var(--cover-black);
  }
  .pad-cover {
    position: relative;
    width: 927px;
    height: 1200px;
    overflow: hidden;
  }
  .cover-texture {
    position: absolute;
    inset: 0;
    background:
      radial-gradient(ellipse at 60% 45%, var(--cover-charcoal) 0%, rgba(28,26,25,0) 55%),
      radial-gradient(ellipse at 50% 110%, var(--grunge-grey) 0%, rgba(58,54,52,0) 35%),
      radial-gradient(ellipse at 100% 30%, rgba(58,54,52,0.6) 0%, rgba(58,54,52,0) 30%),
      var(--cover-black);
  }
  .corner-swoosh {
    position: absolute;
    left: -60px;
    top: -40px;
    width: 260px;
    height: 200px;
    border-radius: 50%;
    background: radial-gradient(ellipse at 40% 40%, #3b3a3a 0%, #1d1c1c 70%, rgba(29,28,28,0) 100%);
  }
  .binding-holes {
    position: absolute;
    left: 0;
    top: 0;
    width: 927px;
    height: 40px;
  }
  .cover-title {
    position: absolute;
    left: 0;
    top: 0;
    width: 927px;
    height: 1200px;
  }
  .title-script {
    font-family: "Parisienne", cursive;
    font-size: 190px;
    fill: var(--title-gold);
  }
  .title-caps {
    font-family: "Marcellus", serif;
    font-size: 200px;
    fill: var(--title-gold);
  }
</style>
</head>
<body>
  <main class="pad-cover">
    <div class="cover-texture" role="img" aria-label="Black distressed grunge background with faint grey ink splatters and swirl ornaments"></div>
    <div class="corner-swoosh" role="img" aria-label="Faint grey curved flourish in the top left corner"></div>

    <svg class="binding-holes" viewBox="0 0 927 40" aria-hidden="true">
      <defs>
        <pattern id="hole-row" x="4" y="0" width="19.6" height="40" patternUnits="userSpaceOnUse">
          <circle cx="9.8" cy="20" r="6.2" fill="var(--binding-hole)"/>
        </pattern>
      </defs>
      <rect x="0" y="0" width="927" height="40" fill="url(#hole-row)"/>
    </svg>

    <svg class="cover-title" viewBox="0 0 927 1200">
      <text class="title-script" x="463" y="436" text-anchor="middle">Amber</text>
      <text class="title-caps" x="463" y="676" text-anchor="middle" textLength="720" lengthAdjust="spacingAndGlyphs">LANTERN</text>
    </svg>
  </main>
</body>
</html>
```